Business Card Design

We need a business card design for a kids clothes shop in Ireland called "Tiny Trotz". Would prefer the colours Lime Green and Dark Purple to be used but are open to suggestions. The logo should include a "Cool" penguin with clothes on.

Industry/Entity Type

Shop

Contact Information for Business Card

Tiny Trotz
Harlow Arcade,
Ashvale Road, Childrenswear 0-12yrs
Kilbrannagh,
XQ82 5LW. Deirdre Walsh.

```html
<!DOCTYPE html>
<html lang="en">
<head>
<meta charset="utf-8">
<title>Tiny Trotz – Business Card</title>
<link href="https://fonts.googleapis.com/css2?family=Tinos:wght@700&display=swap" rel="stylesheet">
<style>
  :root {
    --bg: #e9e9ea;
    --lime: #66bf44;
    --purple: #5a2345;
    --white: #ffffff;
  }
  html, body {
    margin: 0;
    width: 1200px;
    height: 900px;
    overflow: hidden;
    background: var(--bg);
    font-family: "Tinos", "Times New Roman", serif;
    font-weight: 700;
  }
  p { margin: 0; }
  .stage {
    position: relative;
    width: 1200px;
    height: 900px;
  }
  .card {
    position: absolute;
    top: 295px;
    width: 540px;
    height: 310px;
    border-radius: 22px;
    overflow: hidden;
    box-shadow: 0 8px 24px rgba(0,0,0,0.12);
  }
  .card--front { left: 40px; background: var(--lime); }
  .card--back  { left: 620px; background: var(--white); }

  .card__bg { position: absolute; inset: 0; }

  .decor-mascot {
    position: absolute;
    border-radius: 30px;
  }
  .card--front .decor-mascot {
    left: -20px; top: 20px; width: 180px; height: 270px;
    background: linear-gradient(180deg, rgba(255,255,255,0.12), rgba(90,35,69,0.08));
  }
  .card--back .decor-mascot {
    left: -20px; top: 20px; width: 170px; height: 270px;
    background: linear-gradient(180deg, rgba(60,60,60,0.05), rgba(102,191,68,0.08));
  }

  .mascot {
    position: absolute;
    border-radius: 18px;
    background: radial-gradient(circle at 50% 40%, rgba(102,191,68,0.55), rgba(90,35,69,0.55));
  }
  .card--front .mascot { left: 400px; top: 165px; width: 85px; height: 80px; }
  .card--back  .mascot { left: 60px; top: 40px; width: 140px; height: 150px; }

  .brand {
    position: absolute;
    color: var(--purple);
    white-space: nowrap;
    display: flex;
    align-items: center;
    gap: 8px;
  }
  .brand__dot {
    display: inline-block;
    border-radius: 50%;
  }
  .card--front .brand { left: 372px; top: 254px; font-size: 25px; }
  .card--front .brand__dot { width: 10px; height: 10px; background: var(--purple); }
  .card--back .brand { left: 24px; top: 206px; font-size: 30px; }
  .card--back .brand__dot { width: 12px; height: 12px; background: var(--lime); }

  .front__name {
    position: absolute; left: 160px; top: 88px;
    font-size: 25px; color: var(--purple);
  }
  .front__email {
    position: absolute; left: 110px; top: 160px;
    font-size: 17px; color: var(--white);
  }

  .back__name {
    position: absolute; right: 30px; top: 42px;
    font-size: 22px; color: var(--lime);
  }
  .back__trade {
    position: absolute; right: 28px; top: 150px;
    font-size: 17px; color: var(--lime);
  }
  .back__address {
    position: absolute; right: 28px; top: 220px;
    font-size: 15px; line-height: 1.3; color: var(--white);
    text-align: center;
  }
</style>
</head>
<body>
<main class="stage">

  <section class="card card--front" aria-label="Card front">
    <div class="decor-mascot" role="img" aria-label="Faint large penguin mascot decoration"></div>
    <p class="front__name">Deirdre Walsh</p>
    <p class="front__email">deirdrewalsh75@mailbox.ie</p>
    <div class="mascot" role="img" aria-label="Cool penguin mascot wearing a hoodie and sunglasses"></div>
    <div class="brand"><span class="brand__dot"></span>Tiny Trotz</div>
  </section>

  <section class="card card--back" aria-label="Card back">
    <svg class="card__bg" viewBox="0 0 540 310" width="540" height="310" aria-hidden="true">
      <path d="M262 0 C 250 110, 225 220, 190 310 L 205 310 C 245 220, 272 110, 300 0 Z" fill="var(--lime)"/>
      <path d="M312 0 C 285 110, 252 220, 212 310 L 540 310 L 540 0 Z" fill="var(--purple)"/>
    </svg>
    <div class="decor-mascot" role="img" aria-label="Faint large penguin mascot decoration"></div>
    <div class="mascot" role="img" aria-label="Cool penguin mascot wearing a hoodie and sunglasses"></div>
    <div class="brand"><span class="brand__dot"></span>Tiny Trotz</div>
    <p class="back__name">Deirdre Walsh</p>
    <p class="back__trade">Childrenswear 0-12yrs</p>
    <p class="back__address">Harlow Arcade, Ashvale Road<br>Kilbrannagh,<br>XQ82 5LW.</p>
  </section>

</main>
</body>
</html>
```